Design a creative packaging for dog bed

We need a creative packaging design for a dog bed with handle/strap for our new company called SnugHarbor (attacged are the logo). Our bed has several range of size with the biggest are 90 cm x 60 cm x 15 cm with a weight of approximately 5kg. As every bedding comes with a small pillow/plush toy, thus preferable there would be a small compartment where i could place it.

I would need a design that will have 'pastel colors (soft pink and soft blue' and provide a solution to a multi-size bed with only 1 type of packaging.

I am open to a box design & plastic design but the design must be easy to construct and attractive.

Target Market(s)

Age above 30 with middle to higher income range.

Industry/Entity Type

Pet

Font styles to use
Serif
Decorative

Colors
85cae6
f9d9e8

Requirements
Must have
• Creative
• Engaging

```html
<!DOCTYPE html>
<html lang="en">
<head>
<meta charset="utf-8">
<title>SnugHarbor Pet Bed Packaging</title>
<link rel="stylesheet" href="https://fonts.googleapis.com/css2?family=Josefin+Sans:wght@400&family=Handlee&family=Questrial&display=swap">
<style>
  :root {
    --backdrop: #e3e5e7;
    --box-pink: #e2b3b7;
    --handle-pink: #f2d2d6;
    --line-white: #ffffff;
    --feature-gold: #f4d37e;
    --text-white: #ffffff;
    --shadow-grey: #8f8f93;
    --photo-warm: #e9dccf;
    --photo-pink: #f0a9b8;
  }
  html, body {
    margin: 0;
    padding: 0;
    width: 1200px;
    height: 1094px;
    overflow: hidden;
    background: var(--backdrop);
  }
  .canvas {
    position: relative;
    width: 1200px;
    height: 1094px;
  }
  .handle {
    position: absolute;
    left: 500px;
    top: 120px;
    width: 200px;
    height: 170px;
    background: var(--handle-pink);
    border-radius: 18px 18px 0 0;
  }
  .handle-grip {
    position: absolute;
    left: 40px;
    top: 32px;
    width: 120px;
    height: 56px;
    border-radius: 14px;
    background: var(--backdrop);
    box-shadow: inset 0 0 0 4px #6d6d72;
  }
  .front-panel {
    position: absolute;
    left: 100px;
    top: 280px;
    width: 1000px;
    height: 660px;
    background: var(--box-pink);
  }
  .panel-frame {
    position: absolute;
    inset: 22px;
    border: 3px solid var(--line-white);
  }
  .brand-name {
    position: absolute;
    left: 150px;
    top: 270px;
    width: 380px;
    text-align: center;
    font-family: "Josefin Sans", sans-serif;
    font-size: 32px;
    letter-spacing: 2px;
    color: var(--text-white);
    margin: 0;
  }
  .brand-dot {
    display: inline-block;
    width: 14px;
    height: 14px;
    border-radius: 50%;
    background: var(--text-white);
    margin-right: 10px;
    vertical-align: 3px;
  }
  .product-title {
    position: absolute;
    left: 120px;
    top: 320px;
    width: 440px;
    text-align: center;
    font-family: "Handlee", cursive;
    font-size: 118px;
    line-height: 1;
    color: var(--text-white);
    text-shadow: 4px 4px 0 var(--shadow-grey);
    margin: 0;
  }
  .tagline {
    position: absolute;
    left: 120px;
    top: 450px;
    width: 440px;
    text-align: center;
    font-family: "Questrial", sans-serif;
    font-size: 25px;
    letter-spacing: 1px;
    color: var(--text-white);
    margin: 0;
  }
  .pet-silhouette {
    position: absolute;
    left: 118px;
    top: 555px;
    width: 72px;
    height: 76px;
    border-radius: 10px;
    background: rgba(255, 255, 255, 0.85);
  }
  .feature-list {
    position: absolute;
    left: 210px;
    top: 540px;
    list-style: none;
    margin: 0;
    padding: 0;
    font-family: "Questrial", sans-serif;
    font-size: 17px;
    text-transform: uppercase;
  }
  .feature-list li {
    display: flex;
    align-items: center;
    gap: 10px;
    height: 30px;
    color: var(--feature-gold);
  }
  .feature-list li.washable { color: var(--text-white); }
  .feature-icon { width: 20px; height: 20px; flex: none; }
  .zzz {
    width: 20px;
    font-size: 13px;
    color: var(--feature-gold);
    line-height: 1;
    font-weight: bold;
  }
  .product-photo {
    position: absolute;
    left: 570px;
    top: 200px;
    width: 400px;
    height: 420px;
    border-radius: 120px 140px 100px 110px;
    border: 4px solid var(--line-white);
    background: linear-gradient(160deg, var(--photo-warm) 0%, #d9c8b8 50%, var(--photo-pink) 100%);
  }
  .size-badge {
    position: absolute;
    left: 820px;
    top: 70px;
    width: 170px;
    height: 100px;
    border-radius: 50px;
    background: var(--line-white);
    font-family: "Questrial", sans-serif;
    color: #555558;
    text-align: center;
    font-size: 16px;
    line-height: 22px;
    display: flex;
    flex-direction: column;
    justify-content: center;
  }
</style>
</head>
<body>
<main class="canvas">
  <div class="handle"><div class="handle-grip"></div></div>
  <section class="front-panel">
    <div class="panel-frame"></div>
    <p class="brand-name"><span class="brand-dot"></span>SNUGHARBOR</p>
    <h1 class="product-title">pet bed</h1>
    <p class="tagline">soft &amp; confort for your pet</p>
    <div class="pet-silhouette" role="img" aria-label="White silhouette of a puppy standing"></div>
    <ul class="feature-list">
      <li>
        <svg class="feature-icon" viewBox="0 0 20 20"><polygon points="10,1 12.6,7.2 19,7.6 14,11.8 15.6,18.5 10,14.8 4.4,18.5 6,11.8 1,7.6 7.4,7.2" fill="#f4d37e"/></svg>
        Guaranteed quality
      </li>
      <li class="washable">
        <svg class="feature-icon" viewBox="0 0 20 20"><rect x="2" y="2" width="16" height="16" rx="2" fill="none" stroke="#fff" stroke-width="2"/><circle cx="10" cy="11" r="4" fill="none" stroke="#fff" stroke-width="2"/></svg>
        Machine washable
      </li>
      <li><span class="zzz">Z<sup>z</sup></span>Safe and energy efficient</li>
    </ul>
    <div class="product-photo" role="img" aria-label="Photo of a small dog sitting in a pink striped pet bed in a living room"></div>
    <div class="size-badge"><span>LARGE</span><span>90 x 60 x 15 cm</span></div>
  </section>
</main>
</body>
</html>
```